Torlen Caribbean BANK Website Design with UX/UI

I need a website DEV Design Mock up that can be presented in full HTML. Not code needed...just clickable design.
This is a BANk website.
We wil send some websites we like a bit later.
We need at least 10 pages that are Full HTML and integrated.
I will send more Design requirement details.
but feel free to go for it and be ahead

Hi
This is a Bank.
It will be based in the Caribbean. Please read up a bit about the Caribbean so you appreciate our region.
Therefore the only ethnicity that can be used is African American. Go to pixelmarta and search African American People so you can see the ethnicity of the people whom you must feature

The colour Scheme will be those of the Logo. The pantones were provided but it is the BLUE and Yellowish Orange

Target Market(s)

All Bank Customers

Industry/Entity Type

Banking

Number of Pages Required

5+ page

Colors
6b449b
ffc214

Requirements
Must have
• Logo
Follow the Brand Architecture
Use the Pantones provided
Follow the Suite Map Provided
Follow the brief Attached

```html
<!DOCTYPE html>
<html lang="en">
<head>
<meta charset="utf-8">
<title>Torlen Caribbean Bank</title>
<link rel="stylesheet" href="https://fonts.googleapis.com/css2?family=Crimson+Text:wght@400;700&family=Arimo:wght@400;700&display=swap">
<style>
:root{
  --purple:#6b449b;
  --purple-deep:#5a2f96;
  --yellow:#ffc214;
  --ink:#222222;
  --muted:#8a8a8a;
  --cream:#f8f6f3;
  --footer:#1b1b1b;
  --white:#ffffff;
  --footer-text:#dddddd;
}
html,body{margin:0;padding:0;width:1200px;height:4164px;overflow:hidden;background:var(--white);}
body{font-family:"Arimo",Arial,sans-serif;color:var(--ink);}
.page{position:relative;width:1200px;height:4164px;overflow:hidden;}
.abs{position:absolute;}
.serif{font-family:"Crimson Text",Georgia,serif;font-weight:700;}
.btn{position:absolute;display:flex;align-items:center;justify-content:center;font-weight:700;font-size:16px;text-transform:uppercase;text-decoration:none;color:var(--purple);background:var(--yellow);}
.btn-outline{background:transparent;border:3px solid var(--yellow);color:var(--white);box-sizing:border-box;}

/* header */
.topline{top:0;left:0;width:1200px;height:4px;background:var(--purple);}
.header{top:4px;left:0;width:1200px;height:98px;background:var(--white);}
.brand-badge{top:0;left:143px;width:200px;height:178px;border-radius:0 0 100px 100px;background:var(--white);z-index:3;display:flex;align-items:center;justify-content:center;}
.brand-name{font-family:"Crimson Text",Georgia,serif;font-weight:700;font-size:44px;color:var(--purple);line-height:1;margin-top:30px;}
.nav{top:40px;left:424px;display:flex;font-size:16px;z-index:3;}
.nav a{color:#333;text-decoration:none;margin-right:22px;padding:2px 6px;}
.nav a.active{background:var(--purple);color:var(--white);}

/* hero */
.hero{top:102px;left:0;width:1200px;height:740px;background:linear-gradient(100deg,#6f7a3e 0%,#9aa763 28%,#c9c39a 50%,#59515a 75%,#2f3a55 100%);}
.hero-title{top:248px;left:146px;color:var(--white);font-size:66px;line-height:72px;margin:0;text-transform:uppercase;z-index:2;letter-spacing:1px;}
.hero-dots{top:372px;left:1128px;display:flex;flex-direction:column;gap:10px;z-index:2;}
.hero-dots span{width:10px;height:10px;border-radius:50%;background:var(--white);}
.hero-dots span.on{background:var(--yellow);}
.hero-wave{top:730px;left:0;z-index:2;}

/* features */
.features-title{top:906px;left:146px;font-size:46px;margin:0;color:var(--ink);}
.lead{font-size:14px;line-height:30px;color:var(--muted);}
.feature-card{position:absolute;width:168px;height:160px;background:var(--white);box-shadow:0 2px 10px rgba(0,0,0,.12);display:flex;flex-direction:column;align-items:center;justify-content:flex-end;padding-bottom:26px;box-sizing:border-box;font-size:16px;color:#333;}
.feature-card svg{margin-bottom:16px;}
.feature-card.is-active{border-bottom:5px solid var(--yellow);}

/* about */
.about{top:1238px;left:0;width:1200px;height:563px;background:var(--cream);}
.about-photo{top:0;left:0;width:700px;height:563px;background:linear-gradient(90deg,#8a7b6a 0%,#b59a82 40%,#ddd2c4 75%,rgba(248,246,243,0) 100%);}
.play{position:absolute;width:92px;height:92px;border:5px solid var(--white);border-radius:50%;box-sizing:border-box;display:flex;align-items:center;justify-content:center;}
.play::after{content:"";border-left:22px solid var(--white);border-top:14px solid transparent;border-bottom:14px solid transparent;margin-left:6px;}
.about-title{top:1308px;left:665px;margin:0;font-size:46px;line-height:50px;}
.about-title span{display:block;color:var(--purple);}

/* videos */
.videos{top:1801px;left:0;width:1200px;height:607px;background:var(--purple-deep);}
.section-title{left:0;width:1200px;text-align:center;font-size:46px;margin:0;}
.thumb{position:absolute;top:1995px;width:292px;height:198px;}
.thumb .play{left:116px;top:69px;width:60px;height:60px;border-width:3px;}
.thumb .play::after{border-left-width:14px;border-top-width:9px;border-bottom-width:9px;margin-left:4px;}

/* account */
.account{top:2408px;left:0;width:1200px;height:651px;background:linear-gradient(90deg,#f8f4ee 0%,#f3ece3 45%,#c9ab8e 62%,#9c7a63 78%,#e7e1dc 100%);}
.account-title{top:2612px;left:146px;margin:0;font-size:82px;line-height:72px;color:var(--ink);}
.account-title span{display:block;color:var(--purple);}

/* blog */
.blog-card{position:absolute;top:3266px;width:292px;}
.blog-img{height:183px;position:relative;}
.blog-date{position:absolute;left:14px;bottom:12px;color:var(--white);font-weight:700;font-size:16px;}
.blog-avatar{position:absolute;top:216px;left:0;width:48px;height:48px;border-radius:50%;background:#c8c2ba;border:2px solid #e5e5e5;}
.blog-head{position:absolute;top:212px;left:63px;width:228px;font-weight:700;font-size:14px;line-height:20px;color:#444;margin:0;}
.blog-text{position:absolute;top:284px;left:63px;width:228px;font-size:11px;line-height:16px;color:#9a9a9a;margin:0;}
.blog-more{position:absolute;top:326px;left:63px;font-weight:700;font-size:13px;color:var(--purple);text-decoration:none;}
.chev{position:absolute;top:3342px;width:16px;height:16px;border-left:2px solid #bbb;border-bottom:2px solid #bbb;}

/* footer */
.footer-wave{top:3690px;left:0;}
.footer{top:3780px;left:0;width:1200px;height:384px;background:var(--footer);}
.footer-brand{top:3960px;left:146px;width:160px;text-align:center;font-family:"Crimson Text",Georgia,serif;font-weight:700;font-size:54px;line-height:1;color:var(--white);}
.footer-h{top:3866px;font-weight:700;font-size:17px;margin:0;color:var(--white);}
.footer-small{font-size:11px;line-height:19px;color:var(--footer-text);}
.contact-row{position:absolute;left:361px;display:flex;gap:16px;align-items:flex-start;font-size:11px;line-height:19px;color:var(--footer-text);}
.contact-row svg{flex:none;margin-top:3px;}
.news-input{top:3968px;left:618px;width:206px;height:38px;background:var(--white);font-size:10px;color:#666;padding-left:12px;box-sizing:border-box;display:flex;align-items:center;}
.quick{top:3908px;left:918px;margin:0;padding:0;list-style:none;font-size:11px;line-height:22px;color:var(--footer-text);}
.quick li::before{content:"";display:inline-block;border-left:5px solid var(--footer-text);border-top:4px solid transparent;border-bottom:4px solid transparent;margin-right:12px;}
.copyright{top:4112px;left:146px;font-size:11px;color:var(--footer-text);}
.social{top:4102px;left:924px;display:flex;gap:8px;}
.social span{width:26px;height:26px;border:2px solid var(--footer-text);border-radius:50%;box-sizing:border-box;}
</style>
</head>
<body>
<div class="page">

  <div class="abs topline"></div>
  <header class="abs header"></header>
  <div class="abs brand-badge">
    <div class="brand-name">Torlen</div>
  </div>
  <nav class="abs nav">
    <a class="active" href="#">Home</a>
    <a href="#">Personal</a>
    <a href="#">Small Business</a>
    <a href="#">Private Banking</a>
    <a href="#">Corporate</a>
    <a href="#">Wealth</a>
    <a href="#">More</a>
  </nav>

  <section class="abs hero" role="img" aria-label="Photograph of a smiling family outdoors, a father carrying his son on his shoulders"></section>
  <h1 class="abs serif hero-title">Torlen<br>Caribbean<br>Bank</h1>
  <a class="btn" href="#" style="top:514px;left:175px;width:170px;height:44px;z-index:2;">Online Form</a>
  <div class="abs hero-dots"><span></span><span></span><span class="on"></span><span></span><span></span></div>
  <svg class="abs hero-wave" width="1200" height="120" viewBox="0 0 1200 120" aria-hidden="true">
    <path d="M0 72 Q300 10 600 44 Q900 10 1200 72 L1200 120 L0 120 Z" fill="#ffffff"/>
    <path d="M0 60 Q300 -6 600 28 Q900 -6 1200 60" fill="none" stroke="#ffc214" stroke-width="10"/>
    <path d="M0 72 Q300 10 600 44 Q900 10 1200 72" fill="none" stroke="#6b449b" stroke-width="12"/>
  </svg>

  <h2 class="abs serif features-title">FEATURES</h2>
  <p class="abs lead" style="top:988px;left:146px;width:330px;margin:0;">Lorem ipsum dolor sit amet, consectetur adipiscing el do eiusmod tempor incididunt ut dolorucommodo viverra maecenas accumsan lacus vel facilisis.</p>
  <a class="btn" href="#" style="top:1114px;left:146px;width:148px;height:42px;">View More</a>

  <div class="feature-card" style="top:949px;left:514px;">
    <svg width="58" height="58" viewBox="0 0 58 58" fill="none" stroke="#6b449b" stroke-width="2"><rect x="6" y="4" width="30" height="42"/><line x1="12" y1="14" x2="30" y2="14"/><line x1="12" y1="22" x2="30" y2="22"/><rect x="26" y="36" width="26" height="14" rx="3"/><circle cx="32" cy="52" r="3"/><circle cx="46" cy="52" r="3"/></svg>
    Vehicle Loans
  </div>
  <div class="feature-card is-active" style="top:973px;left:700px;">
    <svg width="58" height="58" viewBox="0 0 58 58" fill="none" stroke="#6b449b" stroke-width="2"><path d="M10 28 L29 10 L48 28"/><path d="M16 24 V44 H42 V24"/><circle cx="24" cy="28" r="2"/><circle cx="34" cy="38" r="2"/><line x1="34" y1="26" x2="24" y2="40"/><path d="M6 46 Q18 40 30 48 L50 44"/></svg>
    Mortgages
  </div>
  <div class="feature-card" style="top:949px;left:886px;">
    <svg width="68" height="58" viewBox="0 0 68 58" fill="none" stroke="#6b449b" stroke-width="2"><rect x="4" y="18" width="50" height="30" rx="3"/><line x1="4" y1="26" x2="54" y2="26"/><line x1="10" y1="40" x2="24" y2="40"/><path d="M12 18 L16 8 L62 20 L56 42"/></svg>
    Credit Cards
  </div>

  <section class="abs about">
    <div class="abs about-photo" role="img" aria-label="Photograph of a smiling young woman with earphones working on a laptop"></div>
    <div class="play" style="left:256px;top:236px;"></div>
  </section>
  <h2 class="abs serif about-title">ABOUT<span>Torlen Caribbean Bank</span></h2>
  <p class="abs lead" style="top:1441px;left:665px;width:420px;margin:0;line-height:33px;font-size:14px;">Lorem ipsum dolor sit amet, consectetur adipiscing ed do eiusmod tempor incididunt ut labo dolore magna aliquauis ipsum suspendisse ultrices gravisus commodo viverra maecenas accumsan lacus vel facilorem ipsum dolor sit ansectetur adipiscing ed do eiusmod tempor incididunt ut labo dolore magna aliquauis ipsum</p>
  <a class="btn" href="#" style="top:1674px;left:665px;width:155px;height:40px;">Read More</a>

  <section class="abs videos"></section>
  <h2 class="abs serif section-title" style="top:1896px;color:#fff;">OUR VIDEOS</h2>
  <div class="thumb" style="left:146px;background:linear-gradient(120deg,#3d7fc4,#2a5d98 60%,#1e3f6b);" role="img" aria-label="Video still of two men reviewing paperwork at a desk"><div class="play"></div></div>
  <div class="thumb" style="left:453px;background:linear-gradient(120deg,#dcdcdc,#e9a08e 45%,#b9bcc0);" role="img" aria-label="Video still of a smiling woman holding a tablet in an office"><div class="play"></div></div>
  <div class="thumb" style="left:762px;background:linear-gradient(120deg,#8fb3d6,#d8a98b 50%,#6a8f9e);" role="img" aria-label="Video still of a happy family with two children"><div class="play"></div></div>
  <a class="btn" href="#" style="top:2253px;left:319px;width:270px;height:43px;">Currency Converters</a>
  <a class="btn btn-outline" href="#" style="top:2253px;left:631px;width:284px;height:43px;">Mortgage Calculators</a>

  <section class="abs account" role="img" aria-label="Photograph of a smiling couple relaxing together on a sofa while looking at a tablet"></section>
  <h2 class="abs serif account-title">Get an account<span>That suits you!</span></h2>
  <a class="btn" href="#" style="top:2797px;left:146px;width:190px;height:42px;">Open Account</a>

  <h2 class="abs serif section-title" style="top:3150px;color:var(--ink);">FROM THE BLOG</h2>
  <div class="chev" style="left:90px;transform:rotate(45deg);"></div>
  <div class="chev" style="left:1094px;transform:rotate(-135deg);"></div>

  <article class="blog-card" style="left:133px;">
    <div class="blog-img" style="background:linear-gradient(180deg,#cfcac2,#8d8880 70%,#4a4744);" role="img" aria-label="Photograph of hands signing a document"><span class="blog-date">JUL 23, 2018</span></div>
    <div class="blog-avatar"></div>
    <h3 class="blog-head">Sed ut perspiciatis unde omnis iste natus error sit voluptaccusantium</h3>
    <p class="blog-text">Sed ut perspiciatis unde omnis iste natus error sit voluptatem accusantium</p>
    <a class="blog-more" href="#">READ MORE</a>
  </article>
  <article class="blog-card" style="left:454px;">
    <div class="blog-img" style="background:linear-gradient(180deg,#b8b2a8,#6a4e5a 55%,#3a2e34);" role="img" aria-label="Photograph of a smiling man working at a laptop in an office"><span class="blog-date">MARCH 13 2019</span></div>
    <div class="blog-avatar"></div>
    <h3 class="blog-head">Sed ut perspiciatis unde omnis iste natus error sit voluptaccusantium</h3>
    <p class="blog-text">Sed ut perspiciatis unde omnis iste natus error sit voluptatem accusantium</p>
    <a class="blog-more" href="#">READ MORE</a>
  </article>
  <article class="blog-card" style="left:775px;">
    <div class="blog-img" style="background:linear-gradient(180deg,#d9d4cc,#a08a7a 55%,#3f3a38);" role="img" aria-label="Photograph of a smiling businesswoman in an office"><span class="blog-date">APRIL 05 2020</span></div>
    <div class="blog-avatar"></div>
    <h3 class="blog-head">Sed ut perspiciatis unde omnis iste natus error sit voluptaccusantium</h3>
    <p class="blog-text">Sed ut perspiciatis unde omnis iste natus error sit voluptatem accusantium</p>
    <a class="blog-more" href="#">READ MORE</a>
  </article>

  <svg class="abs footer-wave" width="1200" height="100" viewBox="0 0 1200 100" aria-hidden="true">
    <path d="M0 70 Q300 30 600 10 Q900 30 1200 70 L1200 100 L0 100 Z" fill="#1b1b1b"/>
    <path d="M0 58 Q300 18 600 -2 Q900 18 1200 58" fill="none" stroke="#ffc214" stroke-width="10"/>
    <path d="M0 70 Q300 30 600 10 Q900 30 1200 70" fill="none" stroke="#6b449b" stroke-width="12"/>
  </svg>
  <footer class="abs footer"></footer>
  <div class="abs footer-brand">Torlen</div>

  <h4 class="abs footer-h" style="left:361px;">CONTACT US</h4>
  <div class="contact-row" style="top:3920px;">
    <svg width="12" height="14" viewBox="0 0 12 14"><path d="M6 0 A5 5 0 0 1 11 5 C11 9 6 14 6 14 C6 14 1 9 1 5 A5 5 0 0 1 6 0 Z" fill="#ffc214"/><circle cx="6" cy="5" r="2" fill="#1b1b1b"/></svg>
    <span>23Sed ut perspiciatis unde omnis<br>iste natus error sit voluptatem</span>
  </div>
  <div class="contact-row" style="top:3970px;">
    <svg width="12" height="12" viewBox="0 0 12 12"><path d="M2 0 L5 3 L3.5 5 Q5 8 7 8.5 L9 7 L12 10 L10 12 Q2 11 0 2 Z" fill="#ffc214"/></svg>
    <span>Phone: (888) 555 - 0142</span>
  </div>
  <div class="contact-row" style="top:3998px;">
    <svg width="12" height="10" viewBox="0 0 12 10"><rect width="12" height="10" fill="#ffc214"/><path d="M0 0 L6 5 L12 0" fill="none" stroke="#1b1b1b" stroke-width="1"/></svg>
    <span>info@torlencaribbeanbank.com</span>
  </div>

  <h4 class="abs footer-h" style="left:618px;">SIGN UP NEWSLETTER</h4>
  <p class="abs footer-small" style="top:3914px;left:618px;width:220px;margin:0;">Want to make an impact? Provide your email and we'll be in touch.</p>
  <div class="abs news-input">Enter email</div>
  <a class="btn" href="#" style="top:4022px;left:618px;width:114px;height:34px;font-size:13px;">Sign Up</a>

  <h4 class="abs footer-h" style="left:918px;">QUICK LINKS</h4>
  <ul class="abs quick">
    <li>Home</li><li>Personal</li><li>Small Business</li><li>Private Banking</li><li>Corporate</li><li>Wealth</li>
  </ul>

  <div class="abs copyright">Torlen Caribbean Bank © 2020 All Rights Reserved | Privacy Policy | Terms and Conditions</div>
  <div class="abs social" aria-label="Social links"><span></span><span></span><span></span></div>

</div>
</body>
</html>
```